Business Card Design Project

Business Card
We are rebranding with a new logo
Industry/Entity Type
Business
Contact Information for Business Card
Dennis Marlow +61 427581962 dennis@qovo.com.au P.O. Box 872 Kelvindale QLD 4309
Requirements
Must have
- Logo

```html
<!DOCTYPE html>
<html lang="en">
<head>
<meta charset="utf-8">
<title>Qovo International – Business Card</title>
<link rel="stylesheet" href="https://fonts.googleapis.com/css2?family=Open+Sans:wght@400;600;700&display=swap">
<style>
  :root {
    --backdrop: #3b3431;
    --card: #161718;
    --accent-blue: #2f9fd8;
    --accent-orange: #e8812a;
    --text-light: #e9e9e9;
    --text-muted: #8a8c8f;
    --foil: #9a9c9f;
    --rule: #6d6f72;
  }
  * { box-sizing: border-box; margin: 0; padding: 0; }
  html, body {
    width: 1200px;
    height: 864px;
    overflow: hidden;
    background: var(--backdrop);
    font-family: "Open Sans", Arial, sans-serif;
  }
  .canvas {
    position: relative;
    width: 1200px;
    height: 864px;
  }
  .card {
    position: absolute;
    width: 525px;
    height: 300px;
    background: var(--card);
    border-radius: 3px;
    box-shadow: 0 14px 30px rgba(0,0,0,.45);
    overflow: hidden;
  }
  /* Front side */
  .card--front { left: 70px; top: 100px; }
  .front-brand {
    position: absolute;
    left: 0; right: 0; top: 108px;
    text-align: center;
    color: var(--foil);
    font-weight: 700;
    font-size: 34px;
    letter-spacing: 4px;
    line-height: 1;
  }
  .front-url {
    position: absolute;
    left: 0; right: 0; top: 196px;
    text-align: center;
    color: var(--text-muted);
    font-size: 13px;
    letter-spacing: 7px;
  }
  /* Back side */
  .card--back { left: 605px; top: 440px; }
  .holder-name {
    position: absolute;
    left: 26px; top: 168px;
    color: var(--accent-blue);
    font-weight: 700;
    font-size: 14px;
    line-height: 18px;
    letter-spacing: .5px;
    text-transform: uppercase;
  }
  .card-rule {
    position: absolute;
    left: 26px; right: 26px; top: 192px;
    height: 1px;
    background: var(--rule);
  }
  .contact-list {
    position: absolute;
    left: 26px; top: 202px;
    list-style: none;
  }
  .contact-list li {
    display: flex;
    align-items: center;
    gap: 8px;
    color: var(--text-light);
    font-size: 13px;
    line-height: 21px;
  }
  .contact-icon { width: 12px; height: 12px; flex: none; }
  .brand-mark {
    position: absolute;
    right: 26px; top: 148px;
    display: flex;
    align-items: center;
    gap: 8px;
  }
  .brand-dot {
    width: 12px; height: 12px;
    border-radius: 50%;
    background: var(--accent-orange);
  }
  .brand-name {
    color: var(--accent-blue);
    font-weight: 700;
    font-size: 20px;
    line-height: 26px;
    letter-spacing: 2px;
  }
  .postal-address {
    position: absolute;
    right: 26px; top: 218px;
    text-align: right;
    color: var(--text-light);
    font-size: 15px;
    line-height: 20px;
    font-style: normal;
  }
</style>
</head>
<body>
<main class="canvas">
  <section class="card card--front" aria-label="Card front">
    <p class="front-brand">QOVO INTERNATIONAL</p>
    <p class="front-url">www.qovo.com.au</p>
  </section>

  <section class="card card--back" aria-label="Card back">
    <div class="brand-mark">
      <span class="brand-dot"></span>
      <span class="brand-name">QOVO INTERNATIONAL</span>
    </div>
    <h1 class="holder-name">Dennis Marlow</h1>
    <div class="card-rule"></div>
    <ul class="contact-list">
      <li>
        <svg class="contact-icon" viewBox="0 0 12 12" aria-hidden="true">
          <path d="M2 1.5h2l1 2.5-1.3 1a6 6 0 0 0 3.3 3.3l1-1.3 2.5 1v2a1 1 0 0 1-1 1A9 9 0 0 1 1 2.5a1 1 0 0 1 1-1z" fill="var(--accent-blue)"/>
        </svg>
        +61 427581962
      </li>
      <li>
        <svg class="contact-icon" viewBox="0 0 12 12" aria-hidden="true">
          <rect x="0.5" y="2.5" width="11" height="7.5" rx="1" fill="var(--accent-blue)"/>
          <path d="M1 3l5 3.6L11 3" fill="none" stroke="var(--card)" stroke-width="1"/>
        </svg>
        dennis@qovo.com.au
      </li>
      <li>
        <svg class="contact-icon" viewBox="0 0 12 12" aria-hidden="true">
          <circle cx="6" cy="6" r="5.5" fill="var(--accent-blue)"/>
          <path d="M.5 6h11M6 .5c-2.5 3-2.5 8 0 11M6 .5c2.5 3 2.5 8 0 11" fill="none" stroke="var(--card)" stroke-width=".8"/>
        </svg>
        www.qovo.com.au
      </li>
    </ul>
    <address class="postal-address">P.O. Box 872<br>Kelvindale QLD 4309</address>
  </section>
</main>
</body>
</html>
```